BHAG Poster

We like creativity and visual boxes and shapes not just bullet points. We think we want it to be landscape view. Here are some of the parameters:

BHAG:
Become one of the most admired construction companies in the markets we serve within the next 10 years

3 – 5 year goals:
1. Generate 35m in revenue by 2020
2. Have a 50/50 mix of Public-Private job mix
3. Maintain 15% annual growth

1 year goals:
1. $24M in revenue with better margins
2. 14% gross margin on year
3. Business development begins to pay off
4. Continue recruiting great & talented people

Dynamic Quarter Goal:
(Leave this area blank so we can fill it in each quarter please)

Industry/Entity Type

Landscape

Colors
0355a3

Requirements
Must have
• SHAPES OR BOXES FOR VISUAL EFFECT. We don't want it to just be words on a page. Must be creative. Must have our logo somewhere on the poster. Our cmyk blue color is 100-80-0-22. Poster can have different colors, but it just needs to have some of our blue in it.
Should not have
• no bullet points

```html
<!DOCTYPE html>
<html lang="en">
<head>
<meta charset="utf-8">
<title>BHAG Poster – Hollis Construction</title>
<link href="https://fonts.googleapis.com/css2?family=Lato:wght@400;700;900&family=Black+Ops+One&display=swap" rel="stylesheet">
<style>
  :root{
    --brand-blue:#1f3b93;
    --hazard-yellow:#f2c312;
    --hazard-black:#141414;
    --paper:#ffffff;
    --concrete-light:#f3f3f3;
    --concrete-mid:#dcdcdc;
    --ink:#222222;
    --ink-soft:#555555;
    --backdrop:#e9e9e9;
  }
  html,body{margin:0;width:1200px;height:1200px;overflow:hidden;background:var(--backdrop);}
  .poster{
    position:absolute;left:40px;top:200px;
    width:1325px;height:945px;
    transform:scale(0.8453);transform-origin:0 0;
    background:var(--paper);
    font-family:'Lato',sans-serif;
    box-shadow:0 4px 14px rgba(0,0,0,.18);
    overflow:hidden;
  }
  .poster-shapes{position:absolute;left:0;top:0;}
  .mission{
    position:absolute;left:640px;top:48px;width:672px;text-align:center;
    color:var(--ink-soft);font-size:31px;line-height:37px;margin:0;font-weight:400;
  }
  .mission strong{display:block;color:#000;font-weight:700;font-size:35px;line-height:44px;}
  .mission .accent{color:var(--brand-blue);}
  .bhag-title{
    position:absolute;left:46px;top:92px;margin:0;
    font-family:'Black Ops One',sans-serif;font-weight:400;
    font-size:100px;line-height:1;color:var(--brand-blue);letter-spacing:2px;
  }
  .goals{position:absolute;left:49px;width:520px;margin:0;}
  .goals h2{margin:0;font-size:23px;font-weight:700;color:var(--brand-blue);line-height:30px;}
  .goals p{margin:0;font-size:22px;color:var(--ink-soft);}
  .goals-long{top:219px;}
  .goals-long p{line-height:30px;}
  .goals-short{top:362px;}
  .goals-short h2{margin-bottom:2px;}
  .goals-short p{line-height:33px;}
  .quarter{position:absolute;left:50px;top:580px;width:760px;color:#fff;}
  .quarter h2{margin:0 0 12px;font-size:20px;font-weight:700;}
  .quarter p{margin:0;font-size:13.6px;line-height:18.5px;text-align:justify;}
  .contact{position:absolute;margin:0;padding:0;list-style:none;color:var(--ink-soft);}
  .contact li{position:relative;padding-left:31px;}
  .contact svg{position:absolute;left:0;}
  .contact-phone{left:66px;top:813px;}
  .contact-phone li{font-size:19px;line-height:32px;}
  .contact-phone li.web{font-size:15px;}
  .contact-address{left:370px;top:813px;}
  .contact-address li{font-size:15px;line-height:19px;margin-bottom:11px;}
  .brand{position:absolute;left:912px;top:815px;display:flex;align-items:center;gap:14px;}
  .brand-square{width:82px;height:82px;background:var(--brand-blue);}
  .brand-name{font-family:'Lato',sans-serif;font-weight:900;color:var(--brand-blue);font-size:40px;line-height:40px;letter-spacing:1px;}
  .brand-name span{display:block;font-size:24px;line-height:30px;letter-spacing:2px;}
</style>
</head>
<body>
<article class="poster">
  <svg class="poster-shapes" width="1325" height="945" viewBox="0 0 1325 945">
    <defs>
      <linearGradient id="concrete" x1="0" y1="0" x2="1" y2="1">
        <stop offset="0" stop-color="var(--concrete-mid)"/>
        <stop offset=".5" stop-color="var(--concrete-light)"/>
        <stop offset="1" stop-color="#e4e4e4"/>
      </linearGradient>
      <linearGradient id="site-photo" x1="0" y1="0" x2="0" y2="1">
        <stop offset="0" stop-color="#c9d3dd"/>
        <stop offset=".45" stop-color="#b7ab95"/>
        <stop offset="1" stop-color="#8d887e"/>
      </linearGradient>
      <pattern id="hazard" width="90" height="90" patternUnits="userSpaceOnUse" patternTransform="rotate(45)">
        <rect width="90" height="90" fill="var(--hazard-black)"/>
        <rect width="45" height="90" fill="var(--hazard-yellow)"/>
      </pattern>
      <pattern id="hazard-slim" width="60" height="60" patternUnits="userSpaceOnUse" patternTransform="rotate(-45)">
        <rect width="60" height="60" fill="var(--hazard-black)"/>
        <rect width="30" height="60" fill="var(--hazard-yellow)"/>
      </pattern>
    </defs>
    <rect class="concrete-field" x="0" y="0" width="1000" height="568" fill="url(#concrete)"/>
    <polygon class="header-field" points="425,0 1325,0 1325,205 655,205" fill="var(--paper)"/>
    <polygon class="site-photo" role="img" aria-label="Photo of a construction crew and excavators working on a downtown street" points="440,205 1325,205 1325,740 980,740" fill="url(#site-photo)"/>
    <polygon class="blue-wedge" points="225,0 425,0 655,205 440,205" fill="var(--brand-blue)"/>
    <polygon class="hazard-wedge" points="425,0 515,0 738,205 655,205" fill="url(#hazard-slim)"/>
    <polygon class="quarter-band" points="0,568 808,568 980,740 0,740" fill="var(--brand-blue)"/>
    <line x1="0" y1="566" x2="806" y2="566" stroke="#fff" stroke-width="3"/>
    <rect class="hazard-band" x="0" y="740" width="1325" height="44" fill="url(#hazard)"/>
  </svg>

  <h2 class="mission">Become one of the most admired construction companies in the markets we serve
    <strong>within the next <span class="accent">10 years</span></strong></h2>

  <h1 class="bhag-title">BHAG</h1>

  <section class="goals goals-long">
    <h2>3 – 5 year goals</h2>
    <p>Generate 35m in revenue by 2020</p>
    <p>Have a 50/50 mix of Public-Private job mix</p>
    <p>Maintain 15% annual growth</p>
  </section>

  <section class="goals goals-short">
    <h2>1 year goals:</h2>
    <p>$24M in revenue with better margins</p>
    <p>14% gross margin on year</p>
    <p>Business development begins to pay off</p>
    <p>Continue recruiting great &amp; talented people</p>
  </section>

  <section class="quarter">
    <h2>Dynamic Quarter Goal:</h2>
    <p>Lorem Ipsum is simply dummy text of the printing and typesetting industry. Lorem Ipsum has been the industry's standard dummy text ever since the 1500s, when an unknown printer took a galley of type and scrambled it to make a type specimen book. It has survived not only five centuries, but also the leap into electronic typesetting, remaining essentially unchanged. It was popularised in the 1960s with the release of Letraset sheets containing Lorem Ipsum passages, and more recently with desktop publishing software like Aldus PageMaker including versions of Lorem Ipsum</p>
  </section>

  <ul class="contact contact-phone">
    <li><svg width="16" height="16" viewBox="0 0 16 16" style="top:8px"><path d="M3 1l3 3-2 2c1 2 3 4 5 5l2-2 3 3-2 3C7 15 1 9 1 3z" fill="var(--brand-blue)"/></svg>555.014.2225</li>
    <li><svg width="16" height="16" viewBox="0 0 16 16" style="top:8px"><rect x="4" y="1" width="8" height="4" fill="var(--brand-blue)"/><rect x="1" y="6" width="14" height="6" rx="1" fill="var(--brand-blue)"/><rect x="4" y="10" width="8" height="5" fill="var(--brand-blue)" stroke="#fff"/></svg>555.014.2202</li>
    <li class="web"><svg width="16" height="16" viewBox="0 0 16 16" style="top:8px"><circle cx="8" cy="8" r="6.5" fill="none" stroke="var(--brand-blue)" stroke-width="2"/><path d="M1.5 8h13M8 1.5c-3 3-3 10 0 13M8 1.5c3 3 3 10 0 13" fill="none" stroke="var(--brand-blue)" stroke-width="1.3"/></svg>www.hollisconstruction.com</li>
  </ul>

  <ul class="contact contact-address">
    <li><svg width="16" height="14" viewBox="0 0 16 14" style="top:3px"><rect x="1" y="2" width="14" height="10" fill="var(--brand-blue)"/><path d="M1 2l7 6 7-6" fill="none" stroke="#fff" stroke-width="1.5"/></svg>Hollis Construction Services, Inc.<br>Post Office Box 2210 Linden Falls, Ohio 45000</li>
    <li><svg width="14" height="18" viewBox="0 0 14 18" style="top:2px"><path d="M7 1a6 6 0 0 1 6 6c0 4-6 10-6 10S1 11 1 7a6 6 0 0 1 6-6z" fill="var(--brand-blue)"/><circle cx="7" cy="7" r="2.2" fill="#fff"/></svg>Hollis Construction Services, Inc. 880 Quarry<br>Park Road Linden Falls, Ohio 45001</li>
  </ul>

  <div class="brand">
    <div class="brand-square"></div>
    <div class="brand-name">HOLLIS<span>CONSTRUCTION</span></div>
  </div>
</article>
</body>
</html>
```